KU Curiosities

We need a web design for an ecommerce website that sells innovative gadgets. ***We are in the early stages of the business and don't have official products yet, they are being created. so we need to use placeholders and fake content, please email me with any questions regarding this.

The web page must look modern, fresh and simple and include-

• Logo
• My Account & View Cart link
• Menu - Home, Shop, The Latest, About Us, FAQ, Blog, Contact Us
• Promo bar at the top of the page like on: http://www.plumandwren.example/plwr/ (you can use placeholder text for now)
• Search Box
• Chatterpage, Chirpline, Vidstream, Clipboardly and Orbnet+ icons
• Slogan “Amaze your friends”
• Free shipping on orders over $50
• Banner section - for now you can highlight one of the fake products below, focus on free shipping on order over $50 or some kind of fake promotion
• New Arrivals section - highlight these fake products since we don't have products yet so you can use these products as place holders-
1. https://www.brisketbay.example/tech-gadgets/the-vorntap
2. https://www.brisketbay.example/tech-gadgets/lobelatch-earbud-securer
3. https://www.brisketbay.example/tech-gadgets/pestavo-headfoams
• credit card logos
• paytrellis.example seal - https://check.paytrellis.example/ptseal/images/secure90x72.gif

Example websites:
http://www.plumandwren.example/plwr/
https://www.brisketbay.example/
http://www.tinmantles.example/
https://sproutwell.example/
http://zevrodesk.example/
http://www.dallowsco.example/
http://www.vistaframe.example/

Requirements
Must have
• • Logo
• Search Box
• credit card logos

```html
<!DOCTYPE html>
<html lang="en">
<head>
<meta charset="utf-8">
<title>KU Curiosities</title>
<link rel="stylesheet" href="https://fonts.googleapis.com/css2?family=Lato:ital,wght@0,300;0,400;0,700;1,400&display=swap">
<style>
:root{
  --navy:#0f2b5f;
  --brand:#1d4a7d;
  --sky:#4ab3e8;
  --ink:#1b2a4a;
  --grey:#7b7f86;
  --grey-light:#f2f3f5;
  --grey-mid:#d9dadc;
  --line:#b9d3ee;
  --white:#ffffff;
}
*{box-sizing:border-box;margin:0;padding:0}
html,body{width:902px;height:1200px;overflow:hidden;background:var(--white);font-family:"Lato",Arial,sans-serif}
.page{position:relative;width:902px;height:1200px}
.abs{position:absolute}

/* promo bar */
.promo-bar{left:0;top:0;width:902px;height:25px;background:var(--navy)}
.promo-bar .account-strip{position:absolute;left:605px;top:0;width:297px;height:25px;background:var(--sky);clip-path:polygon(8px 0,100% 0,100% 100%,0 100%)}
.promo-text{position:absolute;left:363px;top:5px;color:var(--white);font-size:13px}
.promo-arrows{position:absolute;left:584px;top:9px}
.account-links{position:absolute;left:625px;top:7px;display:flex;font-size:10px;font-weight:700;color:var(--white)}
.account-links span:nth-child(1){width:53px}
.account-links span:nth-child(2){width:77px}

/* header */
.logo{left:103px;top:36px;display:flex;align-items:center;gap:8px}
.logo-dot{width:44px;height:44px;border-radius:50%;background:var(--sky)}
.logo-name{font-size:21px;font-weight:700;color:var(--brand);line-height:1.05;width:100px}
.seal{left:604px;top:43px;width:56px;height:50px;border-radius:50%;background:radial-gradient(circle,#f3d35a,#c99a1d)}
.phone{left:679px;top:37px;display:flex;align-items:center;gap:5px;font-size:16px;font-weight:700;color:var(--ink)}
.cart-pill{left:690px;top:77px;width:108px;height:24px;border-radius:12px;background:#222;display:flex;align-items:center;gap:5px;padding-left:4px;color:var(--white);font-size:8px}
.cart-pill .cart-ico{width:16px;height:16px;border-radius:50%;background:var(--sky)}

/* nav */
.main-nav{left:103px;top:122px;font-size:11px;color:var(--grey)}
.main-nav span{position:absolute;white-space:nowrap}
.main-nav .active{color:var(--navy);font-weight:700}
.main-nav .active::after{content:"";position:absolute;left:0;right:0;top:16px;height:1px;background:var(--sky)}
.search-box{left:656px;top:119px;width:142px;height:17px;border:1px solid #9aa3ad;font-size:8px;font-style:italic;color:#a3a8ae;padding:3px 5px}
.search-box svg{position:absolute;right:4px;top:2px}
.nav-rule{left:103px;top:150px;width:694px;border-top:1px dashed var(--line)}

/* hero */
.hero{left:103px;top:162px;width:695px;height:264px;background:linear-gradient(90deg,#f4f3f2 0%,#e9b98e 18%,#f2a0b4 45%,#9fc4ea 65%,#c9a0e3 85%,#f0eff1 100%)}
.hero-caption{position:absolute;left:0;bottom:0;width:100%;height:36px;background:rgba(255,255,255,.35)}
.hero-caption p{position:absolute;left:7px;top:4px;font-size:22px;font-weight:700;color:var(--white);white-space:nowrap}
.hero-dots{position:absolute;right:76px;top:16px;display:flex;gap:4px}
.hero-dots i{width:8px;height:8px;border-radius:50%;background:var(--white);display:block}

/* offers */
.offer{top:443px;width:330px;height:130px;border:9px solid var(--brand);background:linear-gradient(#f7f8fa,#dde2e8);overflow:hidden}
.offer-left{left:104px}
.offer-right{left:467px;border-color:var(--sky)}
.offer-title{position:absolute;font-size:26px;font-weight:300;color:#2a5d8f;line-height:30px;white-space:nowrap}
.offer-left .offer-title{left:13px;top:3px}
.offer-right .offer-title{right:6px;top:1px;text-align:right}
.clips-photo{position:absolute;left:2px;top:44px;width:138px;height:64px;background:linear-gradient(90deg,#d6dbe2,#b8c0cc,#c9b3b8,#b6c2cf)}
.code-label{position:absolute;left:148px;top:63px;font-size:16px;color:var(--ink)}
.code-chip{position:absolute;left:225px;top:61px;width:74px;height:26px;background:var(--brand);color:var(--white);font-weight:700;font-size:14px;text-align:center;line-height:26px}
.truck-art{position:absolute;left:8px;top:47px;width:114px;height:60px;background:linear-gradient(#a3b5c9,#8ba0b8)}
.shop-btn{position:absolute;left:211px;top:71px;width:95px;height:26px;background:var(--brand);color:var(--white);font-weight:700;font-size:14px;text-align:center;line-height:26px}

/* products area */
.tabs-panel{left:103px;top:636px;width:694px;height:377px;background:var(--grey-light)}
.cat-head{left:103px;top:604px;width:175px;height:32px;background:#eceef1;font-size:12px;font-weight:700;color:var(--brand);padding:9px 0 0 22px;letter-spacing:.3px}
.tab{top:604px;height:32px;background:var(--white);border:1px solid #e3e5e8;border-bottom:none;font-size:11px;font-weight:700;color:#555a61;text-align:center;line-height:31px;letter-spacing:.3px}
.tab-featured{left:278px;width:173px}
.tab-new{left:451px;width:145px}
.cat-divider{left:277px;top:636px;height:377px;border-left:1px dashed #c9cdd3}
.cat-list{left:116px;top:649px;list-style:none;font-size:11px;color:var(--grey)}
.cat-list li{height:22.6px;display:flex;align-items:center;gap:6px}
.cat-list li::before{content:"";width:3px;height:3px;background:var(--sky)}
.cat-list li.current{color:var(--navy);font-weight:700}

.product{width:140px}
.product-photo{position:absolute;left:0;top:0;width:104px;height:104px}
.cart-badge{position:absolute;left:78px;top:-9px;width:32px;height:32px;border-radius:50%;background:var(--sky);display:flex;align-items:center;justify-content:center}
.product-name{position:absolute;left:8px;top:112px;font-size:9.5px;font-weight:700;color:#444a52;white-space:nowrap}
.product-price{position:absolute;left:11px;top:127px;font-size:9px;white-space:nowrap}
.product-price s{color:#555;margin-right:4px}
.product-price b{color:var(--sky);font-weight:400;font-size:10px}
.next-tab{left:772px;top:774px;width:46px;height:68px;background:var(--white);border-radius:8px 0 0 8px;display:flex;align-items:center;justify-content:center}

/* footer */
.footer{left:103px;top:1024px;width:694px;height:136px;background:var(--brand);border-top:2px solid #4e79a8;color:var(--white);overflow:hidden}
.foot-col{position:absolute;top:10px;font-size:8.5px;line-height:12.7px}
.foot-col h4{font-size:10px;font-weight:700;margin-bottom:3px}
.foot-rule{position:absolute;top:12px;height:110px;border-left:1px dashed #7fa0c6}
.newsletter-box{position:absolute;left:297px;top:28px;width:180px;height:30px;background:#e8eaed;padding:6px 5px}
.newsletter-box .field{width:140px;height:17px;background:var(--white);font-size:7px;font-style:italic;color:#9aa0a8;padding:4px 5px}
.newsletter-box .send{position:absolute;right:5px;top:6px;width:28px;height:17px;background:var(--white);display:flex;align-items:center;justify-content:center}
.newsletter-note{position:absolute;left:304px;top:68px;font-size:8px;font-style:italic;color:#dfe7f1}
.social{position:absolute;left:300px;top:88px;display:grid;grid-template-columns:66px 62px 62px;row-gap:6px;font-size:8.5px}
.social span{display:flex;align-items:center;gap:4px;white-space:nowrap}
.social span::before{content:"";flex:none;width:9px;height:9px;border-radius:50%;background:var(--white)}
.footer-mark{position:absolute;left:528px;top:52px;width:150px;text-align:center;font-size:22px;line-height:24px;font-weight:700;color:#3a6597}

.legal-bar{left:103px;top:1160px;width:694px;height:40px;background:var(--grey-mid)}
.copyright{position:absolute;left:20px;top:14px;font-size:10px;color:#555a61}
.secure-label{position:absolute;left:396px;top:16px;font-size:8px;font-weight:700;color:#555a61;letter-spacing:.3px}
.cards{position:absolute;left:486px;top:9px;display:flex;gap:3px}
.cards span{width:30px;height:21px;background:var(--white);border:1px solid #b7bbc1;border-radius:2px;font-size:5.5px;font-weight:700;color:var(--brand);display:flex;align-items:center;justify-content:center;text-align:center;line-height:6px}
</style>
</head>
<body>
<div class="page">

  <div class="abs promo-bar">
    <div class="account-strip"></div>
    <span class="promo-text">Free Shipping on all Orders over $200</span>
    <svg class="promo-arrows" width="14" height="7" viewBox="0 0 14 7"><path d="M0 3.5 5 0v7zM14 3.5 9 0v7z" fill="#fff"/></svg>
    <div class="account-links"><span>Sign In</span><span>My Account</span><span>Checkout</span></div>
  </div>

  <div class="abs logo"><span class="logo-dot"></span><span class="logo-name">KU Curiosities</span></div>
  <div class="abs seal" role="img" aria-label="Payment security seal"></div>
  <div class="abs phone">
    <svg width="19" height="19" viewBox="0 0 20 20"><circle cx="10" cy="10" r="9" fill="none" stroke="#4ab3e8" stroke-width="1.6"/><path d="M7 5.5c-.8.4-1.3 1.3-1 2.4.8 2.7 3 4.9 5.7 5.7 1.1.3 2-.2 2.4-1l-1.6-1.6-1.3.8c-1.2-.6-2.2-1.6-2.8-2.8l.8-1.3z" fill="#4ab3e8"/></svg>
    123-456-7890
  </div>
  <div class="abs cart-pill"><span class="cart-ico"></span>Cart: 0 item(s) - $0.00</div>

  <nav class="abs main-nav">
    <span class="active" style="left:0">Home</span>
    <span style="left:73px">Shop</span>
    <span style="left:144px">The Latest</span>
    <span style="left:238px">About Us</span>
    <span style="left:327px">FAQ</span>
    <span style="left:394px">Blog</span>
    <span style="left:461px">Contact Us</span>
  </nav>
  <div class="abs search-box">Search
    <svg width="12" height="12" viewBox="0 0 12 12"><circle cx="5" cy="5" r="3.6" fill="none" stroke="#3d6fa3" stroke-width="1.5"/><path d="M7.6 7.6 11 11" stroke="#3d6fa3" stroke-width="1.8"/></svg>
  </div>
  <div class="abs nav-rule"></div>

  <section class="abs hero" role="img" aria-label="Photo of five smiling children wearing colourful headphones">
    <div class="hero-caption">
      <p>Amaze your friends</p>
      <div class="hero-dots"><i></i><i></i><i></i><i></i></div>
    </div>
  </section>

  <div class="abs offer offer-left">
    <div class="offer-title">50% OFF on all Vorntaps</div>
    <div class="clips-photo" role="img" aria-label="Row of colourful clip gadgets hanging on a rail"></div>
    <span class="code-label">use code</span>
    <span class="code-chip">AB123</span>
  </div>
  <div class="abs offer offer-right">
    <div class="offer-title">Free Shipping on all<br>Orders over $50</div>
    <div class="truck-art" role="img" aria-label="Delivery truck graphic marked free"></div>
    <span class="shop-btn">Shop Now</span>
  </div>

  <div class="abs tabs-panel"></div>
  <div class="abs cat-head">CATEGORIES</div>
  <div class="abs tab tab-featured">FEATURED PRODUCTS</div>
  <div class="abs tab tab-new">NEW PRODUCTS</div>
  <div class="abs cat-divider"></div>
  <ul class="abs cat-list">
    <li class="current">Lorem ipsum dolor</li>
    <li>Lorem ipsum dolor sit amet</li>
    <li>Lorem ipsum dolor</li>
    <li>Lorem ipsum dolor</li>
    <li>Lorem ipsum dolor</li>
    <li>Lorem ipsum dolor</li>
    <li>Lorem ipsum</li>
    <li>Lorem ipsum</li>
    <li>Lorem ipsum</li>
    <li>Lorem ipsum dolor</li>
    <li>Lorem ipsum dolor</li>
    <li>Lorem ipsum dolor sit</li>
    <li>Lorem ipsum dolor</li>
    <li>Lorem ipsum dolor</li>
    <li>Lorem ipsum dolor</li>
  </ul>

  <div class="abs product" style="left:321px;top:657px">
    <div class="product-photo" role="img" aria-label="Blue earbud securer product" style="background:linear-gradient(135deg,#ffffff,#cfe9f7 50%,#ffffff)"></div>
    <span class="cart-badge"><svg width="16" height="14" viewBox="0 0 16 14"><path d="M0 1h3l2 8h8l2-6H4" fill="none" stroke="#fff" stroke-width="1.5"/><circle cx="6" cy="12" r="1.3" fill="#fff"/><circle cx="12" cy="12" r="1.3" fill="#fff"/></svg></span>
    <span class="product-name">LOREM IPSUM DOL</span>
    <span class="product-price"><s>$152.00</s><b>$140.00</b></span>
  </div>
  <div class="abs product" style="left:476px;top:657px">
    <div class="product-photo" role="img" aria-label="Pink earbud with securer, discount corner" style="background:linear-gradient(135deg,#f4f4f4,#f3b6cf 55%,#e0463a)"></div>
    <span class="cart-badge"><svg width="16" height="14" viewBox="0 0 16 14"><path d="M0 1h3l2 8h8l2-6H4" fill="none" stroke="#fff" stroke-width="1.5"/><circle cx="6" cy="12" r="1.3" fill="#fff"/><circle cx="12" cy="12" r="1.3" fill="#fff"/></svg></span>
    <span class="product-name">LOREM IPSUM DOL</span>
    <span class="product-price"><s>$152.00</s><b>$140.00</b></span>
  </div>
  <div class="abs product" style="left:629px;top:657px">
    <div class="product-photo" role="img" aria-label="Toddler wearing red headphones" style="background:linear-gradient(135deg,#b9d47a,#e5b79a 50%,#3a4658)"></div>
    <span class="cart-badge"><svg width="16" height="14" viewBox="0 0 16 14"><path d="M0 1h3l2 8h8l2-6H4" fill="none" stroke="#fff" stroke-width="1.5"/><circle cx="6" cy="12" r="1.3" fill="#fff"/><circle cx="12" cy="12" r="1.3" fill="#fff"/></svg></span>
    <span class="product-name">LOREM IPSUM DOL</span>
    <span class="product-price"><s>$152.00</s><b>$140.00</b></span>
  </div>
  <div class="abs product" style="left:321px;top:827px">
    <div class="product-photo" role="img" aria-label="Blue kids headphones" style="background:linear-gradient(135deg,#ffffff,#5a8fe0 55%,#ffffff)"></div>
    <span class="cart-badge"><svg width="16" height="14" viewBox="0 0 16 14"><path d="M0 1h3l2 8h8l2-6H4" fill="none" stroke="#fff" stroke-width="1.5"/><circle cx="6" cy="12" r="1.3" fill="#fff"/><circle cx="12" cy="12" r="1.3" fill="#fff"/></svg></span>
    <span class="product-name">LOREM IPSUM DOL</span>
    <span class="product-price"><s>$152.00</s><b>$140.00</b></span>
  </div>
  <div class="abs product" style="left:476px;top:827px">
    <div class="product-photo" role="img" aria-label="Metal clip gadget on a table" style="background:linear-gradient(135deg,#e8e6e1,#c7c9cc 50%,#9c9a96)"></div>
    <span class="cart-badge"><svg width="16" height="14" viewBox="0 0 16 14"><path d="M0 1h3l2 8h8l2-6H4" fill="none" stroke="#fff" stroke-width="1.5"/><circle cx="6" cy="12" r="1.3" fill="#fff"/><circle cx="12" cy="12" r="1.3" fill="#fff"/></svg></span>
    <span class="product-name">LOREM IPSUM DOL</span>
    <span class="product-price"><s>$152.00</s><b>$140.00</b></span>
  </div>
  <div class="abs product" style="left:629px;top:827px">
    <div class="product-photo" role="img" aria-label="Red clip gadget, discount corner" style="background:linear-gradient(135deg,#ffffff,#f0c4c4 50%,#e0463a)"></div>
    <span class="cart-badge"><svg width="16" height="14" viewBox="0 0 16 14"><path d="M0 1h3l2 8h8l2-6H4" fill="none" stroke="#fff" stroke-width="1.5"/><circle cx="6" cy="12" r="1.3" fill="#fff"/><circle cx="12" cy="12" r="1.3" fill="#fff"/></svg></span>
    <span class="product-name">LOREM IPSUM DOL</span>
    <span class="product-price"><s>$152.00</s><b>$140.00</b></span>
  </div>
  <div class="abs next-tab"><svg width="10" height="22" viewBox="0 0 10 22"><path d="M2 2l6 9-6 9" fill="none" stroke="#c4c8cd" stroke-width="2"/></svg></div>

  <footer class="abs footer">
    <div class="foot-col" style="left:20px"><h4>Quick Links</h4>Home<br>Shop<br>The Latest<br>About Us<br>FAQ<br>Blog<br>Contact Us</div>
    <div class="foot-rule" style="left:110px"></div>
    <div class="foot-col" style="left:146px"><h4>Sitemap</h4>Our Story<br>Our Press Coverage<br>Press Contact<br>Customer Services<br>Awards<br>Work With Us<br>Terms &amp; Conditions<br>Privacy Policy</div>
    <div class="foot-rule" style="left:265px"></div>
    <div class="foot-col" style="left:298px"><h4>Sign Up For Our Newsletter</h4></div>
    <div class="newsletter-box"><div class="field">your email...</div>
      <span class="send"><svg width="10" height="7" viewBox="0 0 10 7"><rect x=".5" y=".5" width="9" height="6" fill="none" stroke="#666"/><path d="M.5 .5 5 4l4.5-3.5" fill="none" stroke="#666"/></svg></span>
    </div>
    <span class="newsletter-note">'Leave your email to subscribe'</span>
    <div class="social"><span>Chatterpage</span><span>Chirpline</span><span>Vidstream</span><span>Orbnet+</span><span>Clipboardly</span></div>
    <div class="foot-rule" style="left:511px"></div>
    <span class="footer-mark">KU<br>Curiosities</span>
  </footer>

  <div class="abs legal-bar">
    <span class="copyright">© 2014 KU Curiosities. All Rights Reserved.</span>
    <span class="secure-label">SECURE PAYMENT</span>
    <div class="cards"><span>Cardora</span><span>Pivota</span><span>Travia</span><span>Travia Spark</span><span>Ameri­vault</span><span>Plain Debit</span></div>
  </div>

</div>
</body>
</html>
```